quillnest.com redesign with wireframes, white space and custom form are very important

Need a new two column design that will convert easily to mobile responsive. Lots of white space. Winning design will probably be based on header area and making the custom form stand out. I want the header to be very much like www.tamvorlo.com except the form not to go up into the header.
Here are some of the websites I really like:
www.brisketdoors.com
http://plinkaroofsdirect.com/
http://dorvikamplandings.com/

We buy homes for cash and close fast. Our target is a home seller who is desperate to sell quickly.
I have uploaded my really ugly wireframe and my logo. I also uploaded my photo for the about us box and a possible photo to use for the header.
The copy on the wireframe is what I will be using except for the about us box.

Here is the exact link for video to frame in the top left box.
https://vidnook.example/Qp39xatLbRr

Number of Pages Required

1 page

Font styles to use
Sans Serif

Colors
0592cd
85cae6
eaf1f7
fbee3d
ec1f27

Requirements
Must have
• Everything on wireframe.
• Must use Verdana font and nothing should be smaller than 12 point. Most should be in 14 point. (except maybe inside of form)

```html
<!DOCTYPE html>
<html lang="en">
<head>
<meta charset="utf-8">
<title>quillnest.com — Sell Your Home For Cash</title>
<style>
:root{
  --blue:#0592cd;
  --blue-dark:#0478aa;
  --sky:#85cae6;
  --pale:#eaf1f7;
  --red:#ec1f27;
  --ink:#222;
  --text:#444;
  --line:#d8d8d8;
  --panel:#ececec;
  --page:#f3f3f3;
  --green:#3a9a3a;
  --footer:#111;
  --nav-active:#1d2a33;
}
*{box-sizing:border-box;margin:0;padding:0}
html,body{width:1200px;height:3136px;overflow:hidden}
body{font-family:Verdana,Geneva,sans-serif;color:var(--text);background:#fff;font-size:14px}
.wrap{width:978px;margin:0 auto;position:relative}

/* header */
.site-header{height:134px}
.site-header .wrap{height:134px;display:flex;justify-content:space-between;align-items:center}
.brand{display:flex;align-items:center;gap:12px;font-weight:700;font-size:32px;color:var(--red)}
.brand-mark{width:22px;height:22px;background:var(--red)}
.header-contact{text-align:right}
.social-row{display:flex;gap:5px;justify-content:flex-end;margin-bottom:10px}
.social-row span{width:22px;height:22px;background:var(--blue);display:block}
.phone-line{display:flex;align-items:center;gap:12px;justify-content:flex-end}
.phone-line .note{font-size:15px;color:var(--ink);line-height:1.15}
.phone-line .num{font-size:25px;color:var(--red);display:block}

/* nav */
.main-nav{height:50px;background:var(--blue)}
.main-nav ul{list-style:none;display:flex;height:50px}
.main-nav li{color:#fff;font-size:13px;line-height:50px;text-align:center;border-right:1px solid rgba(255,255,255,.3)}
.main-nav li:nth-child(1){width:73px;background:var(--nav-active)}
.main-nav li:nth-child(2){width:221px}
.main-nav li:nth-child(3){width:192px}
.main-nav li:nth-child(4){width:217px}
.main-nav li:nth-child(5){width:125px}
.main-nav li:nth-child(6){width:148px;border-right:0}

/* hero */
.hero{height:324px;position:relative;background:linear-gradient(#a9dde6 0%,#7fcfd9 60%,#5fbfca 84%,#b7d33b 84%,#b7d33b 92%,#d8e86a 92%)}
.hero .wrap{height:100%}
.hero h1{position:absolute;top:68px;left:0;font-size:36px;line-height:56px;font-weight:400;color:#1e2a30}
.hero h1 b{font-weight:700}
.hero-art{position:absolute;right:0;top:42px;width:390px;height:282px;background:linear-gradient(135deg,#f2c36a,#e57b3a 60%,#a95a3a)}

/* benefits + form */
.intro{height:694px;border-bottom:1px solid var(--line)}
.intro .wrap{display:flex;justify-content:space-between;padding-top:50px}
.intro-copy{width:550px;padding-top:10px}
.intro-copy h2{font-size:20px;font-weight:400;color:var(--ink);line-height:30px;margin-bottom:18px}
.ticks{list-style:none}
.ticks li{font-size:15px;line-height:33px;padding-left:42px;position:relative;color:var(--text)}
.ticks svg{position:absolute;left:10px;top:10px}
.intro-copy .lead{font-size:14px;letter-spacing:-.3px;color:var(--ink);margin:12px 0 0;line-height:22px}
.video{width:489px;height:301px;margin-top:58px;background:linear-gradient(135deg,#3a4654,#1b2129);position:relative}
.video .play{position:absolute;left:216px;top:120px}

.lead-form{width:408px;height:594px;border:4px solid #fff;box-shadow:0 0 0 2px var(--blue),0 6px 10px rgba(0,0,0,.25);background:#fff}
.lead-form h3{background:var(--red);color:#fff;text-align:center;font-size:24px;line-height:34px;padding:8px 14px;font-weight:700;height:84px}
.lead-form .sub{font-size:16px;color:var(--ink);padding:10px 14px 6px;line-height:22px;font-weight:700;height:58px}
.field{margin:9px 14px 0;height:38px;border:2px solid var(--line);font-size:12px;color:#999;padding:9px 10px}
.field-row{display:flex;gap:12px;margin:9px 14px 0}
.field-row .field{margin:0;flex:1}
.field.area{height:121px}
.submit{display:block;margin:18px auto 0;width:318px;height:50px;background:linear-gradient(var(--blue),var(--blue-dark));color:#fff;font-size:18px;text-align:center;line-height:50px;border-radius:4px}

/* main */
.main{height:1630px;background:var(--page);padding-top:54px;overflow:hidden}
.main .wrap{display:flex;justify-content:space-between;align-items:flex-start}
.content{width:533px;background:#fff;border:1px solid var(--line);padding:18px 11px 24px 10px}
.content h2.blue{color:var(--blue);font-size:20px;font-weight:400;line-height:30px}
.content p{font-size:14px;line-height:24px;color:var(--text)}
.content p .tel{color:var(--red)}
.content h2.dark{font-size:20px;color:var(--ink);font-weight:400;line-height:30px;margin:14px 0 8px}
.content .ticks li{font-size:14px;line-height:31px}
.content .ticks svg{top:9px}
.content .ticks li.hot{color:var(--red)}
.content p.help{color:var(--blue);font-size:21px;line-height:31px;margin:16px 0 22px}
.tab{margin-left:-26px;color:#fff;font-size:18px;padding:0 20px;height:44px;line-height:44px}
.tab.red{background:var(--red)}
.tab.blue{background:var(--blue)}
.post{padding:18px 0 14px}
.meta{font-size:12px;color:#666;margin-bottom:12px}
.meta i{font-style:normal;color:var(--blue)}
.post-body{display:flex;gap:12px}
.thumb{width:190px;height:134px;flex:none;background:linear-gradient(#9fc3e4,#b97a5a 45%,#5b8a3d 75%)}
.post-main{display:flex;flex-direction:column;justify-content:space-between;height:134px;flex:1}
.post-text{font-size:13px;line-height:22px;color:var(--text)}
.post-actions{display:flex;justify-content:flex-end}
.post-actions span{font-size:13px;color:#fff;height:30px;line-height:30px;padding:0 12px}
.post-actions .count{background:var(--red)}
.post-actions .reply{background:#222}
.pager{display:flex;gap:8px;margin:12px 0 26px}
.pager span{width:34px;height:34px;background:#222;color:#fff;text-align:center;line-height:34px;font-size:13px}
.pager span.on{background:var(--red)}
.tags{display:flex;flex-wrap:wrap;gap:10px 12px;padding:18px 0 0 16px}
.tags span{background:#222;color:#fff;font-size:15px;padding:0 20px;height:42px;line-height:42px}

.sidebar{width:408px}
.side-top{display:flex;justify-content:space-between;align-items:center}
.btn-privacy{background:var(--blue);color:#fff;font-size:15px;padding:0 16px;height:44px;line-height:44px}
.side-icons{display:flex;gap:10px}
.side-icons span{width:14px;height:14px;background:#aaa;display:block}
.call{font-size:16px;color:var(--ink);font-weight:700;line-height:26px;margin:22px 0 20px;padding-left:8px}
.box{background:var(--panel);border:4px solid #fff;box-shadow:0 0 0 1px var(--line);padding:16px 16px 18px;margin-bottom:26px}
.box h4{font-size:20px;font-weight:400;color:var(--ink);border-bottom:2px dotted #999;padding-bottom:8px;margin-bottom:12px;line-height:30px}
.box p{font-size:14px;line-height:24px;color:var(--text)}
.box p.sig{text-align:right;font-size:15px;margin-top:12px;color:var(--ink)}
.sig b{color:var(--red);font-weight:400}
.about{display:flex;gap:10px}
.about .photo{width:104px;height:150px;flex:none;background:linear-gradient(#7aa7d6,#c69478 55%,#3a5f8f)}
.about h4{border:0}
.cities-grid{display:grid;grid-template-columns:1fr 1fr;column-gap:10px;margin:10px 0 6px;
  background:radial-gradient(ellipse at 55% 45%,rgba(236,31,39,.12),transparent 60%)}
.cities-grid span{font-size:14px;line-height:23.6px;color:var(--ink);display:flex;align-items:center;gap:8px}
.cities-grid span::before{content:"";width:12px;height:12px;border:1px solid #888;background:#fff}
.view-all{text-align:right;font-size:13px;color:var(--ink);text-decoration:underline;margin-bottom:12px}
.box p.red{color:var(--red)}
.buy-photos{display:flex;justify-content:space-between;margin-bottom:12px}
.buy-photos div{width:178px;height:104px;background:linear-gradient(#a6c9e8,#c48a64 50%,#5e8c3e)}

/* footer */
.site-footer{height:304px;background:var(--footer);color:#555;border-top:4px solid #333}
.foot-cols{display:flex;padding-top:22px;height:256px}
.foot-cols div:nth-child(1){width:322px;padding-right:60px}
.foot-cols div:nth-child(2){width:221px}
.foot-cols div:nth-child(3){width:217px}
.foot-cols div:nth-child(4){width:218px}
.foot-cols h5{color:#ddd;font-size:17px;font-weight:700;margin-bottom:22px}
.foot-cols p,.foot-cols li{font-size:14px;line-height:24px;list-style:none}
.foot-cols li span{display:inline-block;width:12px;height:12px;background:#555;margin-right:14px}
.foot-bottom{display:flex;justify-content:space-between;font-size:13px}
</style>
</head>
<body>

<header class="site-header">
  <div class="wrap">
    <div class="brand"><span class="brand-mark"></span>quillnest.com</div>
    <div class="header-contact">
      <div class="social-row"><span></span><span></span><span></span><span></span></div>
      <div class="phone-line">
        <svg width="32" height="32" viewBox="0 0 24 24"><path fill="#333" d="M6.6 10.8a15 15 0 0 0 6.6 6.6l2.2-2.2c.3-.3.7-.4 1-.2 1.1.4 2.3.6 3.6.6.6 0 1 .4 1 1V20c0 .6-.4 1-1 1A17 17 0 0 1 3 4c0-.6.4-1 1-1h3.5c.6 0 1 .4 1 1 0 1.3.2 2.5.6 3.6.1.3 0 .7-.2 1z"/></svg>
        <div class="note">Nights and weekends ok<span class="num">407-555-0142</span></div>
      </div>
    </div>
  </div>
</header>

<nav class="main-nav">
  <div class="wrap">
    <ul>
      <li>HOME</li><li>SELL YOUR HOME</li><li>HOW IT WORKS</li><li>STOP FORECLOSURE</li><li>PROBATE</li><li>CONTACT US</li>
    </ul>
  </div>
</nav>

<section class="hero">
  <div class="wrap">
    <h1>SELL YOUR <b>HOME</b> FOR<br><b>CASH</b> IN 8 DAYS WE BUY<br><b>HOUSES NATIONWIDE</b>.</h1>
    <div class="hero-art" role="img" aria-label="Illustration of a buyer shaking hands with a home seller in front of a house"></div>
  </div>
</section>

<section class="intro">
  <div class="wrap">
    <div class="intro-copy">
      <h2>THESE ARE THE BENEFITS OF SELLING YOUR<br>HOME TO US:</h2>
      <ul class="ticks">
        <li><svg width="18" height="14" viewBox="0 0 18 14"><path d="M1 7l5 5L17 1" fill="none" stroke="#3a9a3a" stroke-width="2.5"/></svg>You pick the closing date.</li>
        <li><svg width="18" height="14" viewBox="0 0 18 14"><path d="M1 7l5 5L17 1" fill="none" stroke="#3a9a3a" stroke-width="2.5"/></svg>You pay NO Commissions or Fees.</li>
        <li><svg width="18" height="14" viewBox="0 0 18 14"><path d="M1 7l5 5L17 1" fill="none" stroke="#3a9a3a" stroke-width="2.5"/></svg>You don't have to paint, clean or make repairs</li>
      </ul>
      <p class="lead">Watch to see our president Marcus explain how easy it is to sell to us:</p>
      <div class="video" role="img" aria-label="Video of the company president explaining the selling process">
        <svg class="play" width="56" height="60" viewBox="0 0 56 60"><path d="M4 4l48 26L4 56z" fill="#ec1f27"/></svg>
      </div>
    </div>

    <form class="lead-form">
      <h3>YES, I WANT TO SELL MY HOME FAST!</h3>
      <p class="sub">Get a no obligation written offer in 36 hours</p>
      <div class="field">Your Name:</div>
      <div class="field">Your Phone Number:</div>
      <div class="field">Your Email Address:</div>
      <div class="field">Property address including City, State &amp; Zip code:</div>
      <div class="field-row"><div class="field">Repairs needed if any:</div><div class="field">Asking Price:</div></div>
      <div class="field area">Comments</div>
      <div class="submit">SUBMIT, TO GET STARTED</div>
    </form>
  </div>
</section>

<section class="main">
  <div class="wrap">
    <article class="content">
      <h2 class="blue">THESE ARE THE BENEFITS OF SELLING YOUR HOME TO US:</h2>
      <p>Selling a home on your own has never been easier. From Orlando to Greensboro - and all points in between- you can sell your home today without any hassles. Call <span class="tel">1-800-555-0198</span> or fill out the form below to get a written offer on your home in just 36 hours. Sell today online to people that care.</p>
      <h2 class="dark">IF YOU NEED TO SELL A HOME FAST<br>BECAUSE OF:</h2>
      <ul class="ticks">
        <li><svg width="18" height="14" viewBox="0 0 18 14"><path d="M1 7l5 5L17 1" fill="none" stroke="#3a9a3a" stroke-width="2.5"/></svg>Divorce or Bankruptcy</li>
        <li><svg width="18" height="14" viewBox="0 0 18 14"><path d="M1 7l5 5L17 1" fill="none" stroke="#3a9a3a" stroke-width="2.5"/></svg>Foreclosure</li>
        <li class="hot"><svg width="18" height="14" viewBox="0 0 18 14"><path d="M1 7l5 5L17 1" fill="none" stroke="#3a9a3a" stroke-width="2.5"/></svg>Landlord problems - evictions with tenants okay</li>
        <li><svg width="18" height="14" viewBox="0 0 18 14"><path d="M1 7l5 5L17 1" fill="none" stroke="#3a9a3a" stroke-width="2.5"/></svg>Inherited property in probate</li>
        <li><svg width="18" height="14" viewBox="0 0 18 14"><path d="M1 7l5 5L17 1" fill="none" stroke="#3a9a3a" stroke-width="2.5"/></svg>Termites, mold, flood or fire damage, leaky roof</li>
        <li><svg width="18" height="14" viewBox="0 0 18 14"><path d="M1 7l5 5L17 1" fill="none" stroke="#3a9a3a" stroke-width="2.5"/></svg>Moving or can't afford mortgage payments</li>
      </ul>
      <p class="help">We Can Help.<br>We are the fastest home buyers around.</p>

      <div class="tab red">Our Blog</div>
      <div class="post">
        <div class="meta">On 02.19.10. &nbsp;In <i>Blog Theme</i>, &nbsp;by <i>admin</i></div>
        <div class="post-body"><div class="thumb" role="img" aria-label="Photo of a brick house with a green lawn"></div>
          <div class="post-main"><div class="post-text">Lorem ipsum dolor sit amet, consectetur adipiscing elit, sed do eiusmod tempor incididunt ut labore et dolore magna aliquaex ea commodo consequat.</div>
          <div class="post-actions"><span class="count">12 Comments</span><span class="reply">Leave your Comments</span></div></div></div>
      </div>
      <div class="post">
        <div class="meta">On 02.19.10. &nbsp;In <i>Blog Theme</i>, &nbsp;by <i>admin</i></div>
        <div class="post-body"><div class="thumb" role="img" aria-label="Photo of a brick house with a green lawn"></div>
          <div class="post-main"><div class="post-text">Lorem ipsum dolor sit amet, consectetur adipiscing elit, sed do eiusmod tempor incididunt ut labore et dolore magna aliquaex ea commodo consequat.</div>
          <div class="post-actions"><span class="count">12 Comments</span><span class="reply">Leave your Comments</span></div></div></div>
      </div>
      <div class="post">
        <div class="meta">On 02.19.10. &nbsp;In <i>Blog Theme</i>, &nbsp;by <i>admin</i></div>
        <div class="post-body"><div class="thumb" role="img" aria-label="Photo of a brick house with a green lawn"></div>
          <div class="post-main"><div class="post-text">Lorem ipsum dolor sit amet, consectetur adipiscing elit, sed do eiusmod tempor incididunt ut labore et dolore magna aliquaex ea commodo consequat.</div>
          <div class="post-actions"><span class="count">12 Comments</span><span class="reply">Leave your Comments</span></div></div></div>
      </div>
      <div class="pager"><span class="on">1</span><span>2</span><span>3</span></div>

      <div class="tab blue">Archives</div>
      <div class="tags"><span>Sell My House</span><span>Fast Cash for Homes</span><span>We Buy Houses</span><span>Real Estate Investor</span><span>Latest</span></div>
    </article>

    <aside class="sidebar">
      <div class="side-top"><span class="btn-privacy">Our Privacy Policy</span><div class="side-icons"><span></span><span></span><span></span><span></span><span></span></div></div>
      <p class="call">CALL US 8AM TO 10 PM EASTERN TIME.<br>WE ANSWER OUR PHONES.</p>

      <div class="box">
        <h4>Home Seller Testimonials</h4>
        <p>I just wanted to thank you for buying my home in Winter Park. You made it fast and easy and kept me well informed the whole way.</p>
        <p class="sig"><b>Dena Holloway</b> – Winter Park</p>
      </div>

      <div class="box about">
        <div><h4>About Us</h4><p>Owned and operated in Orlando Florida since 2001. Oldest Continuous operated website in country.</p></div>
        <div class="photo" role="img" aria-label="Portrait photo of the company owner"></div>
      </div>

      <div class="box">
        <h4>Some of the Cities where we buy houses. Not all are listed.</h4>
        <p>These are the cities where we have an affiliate where you can sell a home fast or quickly and we buy homes:</p>
        <div class="cities-grid">
          <span>Orlando</span><span>Harrisburg</span>
          <span>Jacksonville</span><span>Virginia Beach</span>
          <span>Ft Myers</span><span>Virginia Homes</span>
          <span>Tampa</span><span>Greensboro</span>
          <span>St Pete</span><span>Charleston SC</span>
          <span>Gainesville</span><span>Flint Rochester</span>
          <span>Tallahassee</span><span>Lake Florida</span>
          <span>Melbourne</span><span>Wilmington</span>
          <span>West Palm Beach</span><span>Columbia</span>
          <span>Apopka</span><span>Titusville</span>
          <span>Deland</span><span>Valdosta</span>
          <span>Kissimmee</span><span>Houston</span>
          <span>Camden Atlanta</span><span>Detroit</span>
          <span>San Antonio</span><span>Phoenix</span>
        </div>
        <div class="view-all">View All Cities</div>
        <p class="red">If you don't see your city, we still probably buy homes there.</p>
      </div>

      <div class="box">
        <h4>We Buy</h4>
        <div class="buy-photos">
          <div role="img" aria-label="Photo of a large family house"></div>
          <div role="img" aria-label="Photo of a brick house with a lawn"></div>
        </div>
        <p>We buy nice pretty houses and some ugly ones as well.</p>
      </div>
    </aside>
  </div>
</section>

<footer class="site-footer">
  <div class="wrap">
    <div class="foot-cols">
      <div><h5>WHY US</h5><p>Lorem ipsum dolor sit amet, consectetur adipiscing elit. Aenean libero tortor, auctor et blandit in, facilisis sed nulla. Vivamus condimentum</p></div>
      <div><h5>SITE LINKS</h5><ul><li>Sell Your Home</li><li>How it works</li><li>Stop foreclosure</li><li>Probate</li><li>Contact</li></ul></div>
      <div><h5>GET SOCIAL</h5><ul><li><span></span>Porchlight</li><li><span></span>Chirpline</li><li><span></span>Circlespace</li><li><span></span>Workhall</li></ul></div>
      <div><h5>STAY IN TOUCH</h5><ul><li><span></span>2240 Fernbrook<br>&nbsp;&nbsp;&nbsp;&nbsp;&nbsp;&nbsp;&nbsp;Ave #310 Winter Park<br>&nbsp;&nbsp;&nbsp;&nbsp;&nbsp;&nbsp;&nbsp;FL 32789</li><li><span></span>407-555-0142</li><li><span></span>hello@quillnest.com</li></ul></div>
    </div>
    <div class="foot-bottom"><span>Copyright © 2015 . quillnest.com All right Reserved</span><span>Privacy Policy | Terms &amp; Conditions</span></div>
  </div>
</footer>

</body>
</html>
```